Book cover design about quality management systems

Book cover design that I can display in my website for ore orders
The book is about helping organisations to fully integrate their Quality management systems rather than having a quality system which sits off to the side and adds extra work.
It is aimed at organisations leaders
It is about leaders taking ownership and leading the decision and design of the quality management system and therefore being able to delegate more effectively.

Target Market(s)

CEO of government funded organisations

Industry/Entity Type

Management

Font styles to use
Sans Serif

Colors

Designer to choose colors to be used in the design.

Requirements
Must have
• Ability to be used on website
• Title of the book
• Shape steer sustain
• Strap line - making quality work for you
Nice to have
• Not too fussy
• Not a black cover
• Deep Yellow in the design if possible
Should not have
• Anything too feminine

```html
<!DOCTYPE html>
<html lang="en">
<head>
<meta charset="utf-8">
<title>Shape Steer Sustain – Book Cover</title>
<link rel="stylesheet" href="https://fonts.googleapis.com/css2?family=Roboto+Condensed:wght@800;900&family=Open+Sans:wght@700&display=swap">
<style>
  :root {
    --paper: #ffffff;
    --deep-yellow: #fcbf1e;
    --title-white: #ffffff;
    --title-gold: #9a7418;
    --title-khaki: #8f7b53;
    --strap: #8a7d62;
    --khaki: #928563;
    --runner-dark: #4f4f4f;
    --runner-light: #e6e6e6;
    --runner-red: #c6282f;
  }
  * { margin: 0; padding: 0; box-sizing: border-box; }
  html, body {
    width: 800px;
    height: 1200px;
    overflow: hidden;
    background: var(--paper);
  }
  .cover {
    position: relative;
    width: 800px;
    height: 1200px;
    background: var(--paper);
    overflow: hidden;
  }
  .cover-art {
    position: absolute;
    inset: 0;
    width: 800px;
    height: 1200px;
  }
  .title {
    position: absolute;
    left: 0;
    top: 270px;
    width: 800px;
    text-align: center;
    font-family: "Roboto Condensed", "Arial Narrow", sans-serif;
    font-weight: 900;
    font-size: 132px;
    line-height: 108px;
    letter-spacing: 1px;
    text-transform: uppercase;
  }
  .title-line { display: block; }
  .title-line--first { color: var(--title-white); }
  .title-line--second { color: var(--title-gold); }
  .title-line--third { color: var(--title-khaki); }
  .strapline {
    position: absolute;
    left: 0;
    top: 600px;
    width: 800px;
    text-align: center;
    font-family: "Open Sans", Arial, sans-serif;
    font-weight: 700;
    font-size: 29px;
    color: var(--strap);
  }
  .author {
    position: absolute;
    left: 0;
    top: 1112px;
    width: 800px;
    text-align: center;
    font-family: "Open Sans", Arial, sans-serif;
    font-weight: 700;
    font-size: 54px;
    letter-spacing: 1px;
    color: var(--paper);
    text-transform: uppercase;
  }
</style>
</head>
<body>
  <main class="cover">
    <svg class="cover-art" viewBox="0 0 800 1200" xmlns="http://www.w3.org/2000/svg" aria-hidden="false">
      <defs>
        <linearGradient id="runners-tone" x1="0" y1="0" x2="1" y2="0">
          <stop offset="0" stop-color="var(--runner-dark)"/>
          <stop offset="0.55" stop-color="#6a6a6a"/>
          <stop offset="0.8" stop-color="var(--runner-light)"/>
          <stop offset="0.92" stop-color="var(--runner-red)" stop-opacity="0.55"/>
          <stop offset="1" stop-color="var(--paper)"/>
        </linearGradient>
      </defs>

      <!-- yellow field -->
      <path class="yellow-field" fill="var(--deep-yellow)"
            d="M0,250 C200,170 500,140 800,160 L800,600 C600,720 300,760 0,750 Z"/>

      <!-- thin yellow outer arc at the top -->
      <path class="yellow-arc" fill="none" stroke="var(--deep-yellow)" stroke-width="6"
            d="M120,420 C180,200 400,40 640,38 C720,37 780,45 820,55"/>

      <!-- white crossing arcs over the yellow field -->
      <g class="white-arcs" fill="none" stroke="var(--paper)" stroke-width="5">
        <path d="M-20,210 C150,150 330,150 470,190 C640,240 760,330 820,420"/>
        <path d="M-20,600 C60,640 200,690 380,705 C560,715 720,660 820,600"/>
        <path d="M70,760 C40,560 120,330 300,190 C420,100 560,60 700,60"/>
      </g>

      <!-- khaki base with yellow edge line -->
      <path class="base-edge" fill="none" stroke="var(--deep-yellow)" stroke-width="6"
            d="M0,1000 C300,990 600,920 820,815"/>
      <path class="khaki-base" fill="var(--khaki)"
            d="M0,1012 C300,1005 600,935 800,842 L800,1200 L0,1200 Z"/>

      <!-- illustration area: line of runners following a leader -->
      <path class="runners-illustration" role="img"
            aria-label="Illustration: a crowd of grey figures running in a line behind a single red figure pointing the way forward"
            fill="url(#runners-tone)" opacity="0.9"
            d="M0,800 C200,780 420,760 560,740 C640,725 720,700 780,690 L780,850 C700,880 620,900 540,910 C400,930 200,960 0,975 Z"/>
    </svg>

    <h1 class="title">
      <span class="title-line title-line--first">Shape</span>
      <span class="title-line title-line--second">Steer</span>
      <span class="title-line title-line--third">Sustain</span>
    </h1>
    <p class="strapline">Making quality work for you</p>
    <p class="author">Helena Marsh</p>
  </main>
</body>
</html>
```